4D Little Lumen Luxury Ultrasound Billboard

Design a HIGH-END, MODERN billboard for my private prenatal ultrasound studio, 4D Little Lumen, located in Pace, Florida.
This billboard will be viewed by drivers traveling at highway speeds, so it must be extremely clean, simple, and readable within 6 seconds.
About My Business
4D Little Lumen is a private prenatal ultrasound studio specializing in:
Highest technology 4D/HD Ultrasounds
Early Gender Determination
Pregnancy Confirmation
I have been serving families for nearly 10 years and is known for creating a memorable experience, not just an ultrasound appointment.
Design Style
I DO NOT want:
Flowers
Leaves
Swirls
Glitter
Hearts everywhere
Busy backgrounds
Generic maternity stock graphics
I DO want:
Modern
Luxury
Upscale
Clean
Professional
Eye-catching
Premium medical spa feel
Colors
Use colors from my logo:
LOGO Green ( or a deep green)
Black
White
Soft Gold accents
Images:
Incorporate my professional headshot in a clean, modern way, logo, and the ultrasound images
Text
Keep wording minimal.
Primary Headline ( OPEN TO IDEAS) :
EXAMPLES ( WOULD RATHER SOMETHING MORE CATCHY)
" ADVANCED IMAGING. UNFORGETTABLE MOMENTS"
"MEET YOUR BABY BEFORE BIRTH"
Under headline:
4D Ultrasound • Early Gender • Pregnancy Confirmation
Business Name:
4D Little Lumen
Private Prenatal Ultrasound Studio
Phone Number:
850-471-5923
Important
This billboard must be readable in 5–6 seconds from a moving vehicle.
Less text is better.
The phone number and business name must be visible from a distance.
The design should feel like a premium brand that immediately tells expecting parents:
“This is where I go to see my baby.”
Files Provided
Official logo
Headshot
Ultrasound images
Don’t make this look like a medical office billboard.
Make it look like a luxury baby experience billboard. That’s what separates 4D Little Lumen from hospitals, OB offices, and all the new studios popping up around you. The emotional connection is what gets moms to book. ❤️
Billboard Size - 10.6” x 36”

```html
<!DOCTYPE html>
<html lang="en">
<head>
<meta charset="utf-8">
<title>4D Little Lumen Billboard</title>
<link href="https://fonts.googleapis.com/css2?family=Montserrat:wght@600;700;800&family=Oswald:wght@500&display=swap" rel="stylesheet">
<style>
  :root{
    --sage:#5f6d66;
    --sage-dark:#4f5c56;
    --gold:#99732c;
    --gold-soft:#d8ae4a;
    --paper:#f4f6f5;
    --white:#ffffff;
    --stage:#e6e8e7;
  }
  html,body{margin:0;padding:0;width:1200px;height:1200px;overflow:hidden;background:var(--stage);}
  .canvas{position:relative;width:1200px;height:1200px;}
  .billboard{position:absolute;left:20px;top:430px;width:1160px;height:340px;background:var(--paper);overflow:hidden;box-shadow:0 6px 24px rgba(0,0,0,.18);}
  .scan-window{position:absolute;left:-120px;top:12px;width:316px;height:316px;border-radius:50%;border:6px solid var(--gold-soft);background:radial-gradient(circle at 60% 45%,#d79a86 0%,#b86f5c 45%,#7a3a2c 100%);box-sizing:border-box;}
  .headline{position:absolute;left:200px;top:22px;width:640px;text-align:center;font-family:'Montserrat',sans-serif;font-weight:800;line-height:1;white-space:nowrap;}
  .headline .rule{height:2px;background:linear-gradient(90deg,transparent,var(--gold-soft),transparent);margin:0 40px;}
  .headline .line-one{color:var(--sage);font-size:54px;font-weight:700;margin:8px 0 2px;letter-spacing:-1px;}
  .headline .line-two{color:var(--gold);font-size:46px;margin-bottom:8px;letter-spacing:-0.5px;}
  .services{position:absolute;left:228px;top:180px;width:590px;display:flex;justify-content:space-between;align-items:center;}
  .service{display:flex;align-items:center;gap:8px;}
  .service-icon{width:50px;height:50px;flex:none;}
  .service-label{font-family:'Oswald',sans-serif;font-weight:500;color:var(--sage);font-size:22px;line-height:.98;text-align:center;text-transform:uppercase;white-space:nowrap;}
  .phone-pill{position:absolute;left:240px;top:255px;width:530px;height:62px;border-radius:14px;background:var(--sage);display:flex;align-items:center;}
  .phone-icon{width:34px;height:34px;margin-left:20px;}
  .phone-divider{width:1px;height:40px;background:rgba(0,0,0,.35);margin:0 22px 0 16px;}
  .phone-number{font-family:'Montserrat',sans-serif;font-weight:800;color:var(--white);font-size:52px;letter-spacing:-1px;white-space:nowrap;}
  .headshot{position:absolute;right:0;top:0;width:320px;height:340px;background:linear-gradient(160deg,#e9ecea 0%,#cdd3cf 40%,#6f7f63 75%,#4e5e45 100%);}
  .brand-card{position:absolute;left:833px;top:212px;width:300px;height:112px;background:var(--white);border:3px solid var(--sage);border-radius:14px;box-sizing:border-box;display:flex;flex-direction:column;align-items:center;justify-content:center;gap:6px;}
  .brand-name{font-family:'Montserrat',sans-serif;font-weight:800;color:var(--gold);font-size:30px;letter-spacing:-0.5px;white-space:nowrap;}
  .brand-tagline{font-family:'Montserrat',sans-serif;font-weight:800;color:var(--gold);font-size:11px;letter-spacing:1.5px;text-transform:uppercase;white-space:nowrap;}
</style>
</head>
<body>
<div class="canvas">
  <section class="billboard">
    <div class="scan-window" role="img" aria-label="4D ultrasound image of a baby's face"></div>

    <div class="headline">
      <div class="rule"></div>
      <div class="line-one">THE FIRST LOOK</div>
      <div class="line-two">YOU’LL NEVER FORGET</div>
      <div class="rule"></div>
    </div>

    <div class="services">
      <div class="service">
        <svg class="service-icon" viewBox="0 0 54 54"><circle cx="27" cy="27" r="25" fill="none" stroke="var(--sage)" stroke-width="2"/><circle cx="27" cy="27" r="18" fill="none" stroke="var(--gold)" stroke-width="3"/></svg>
        <div class="service-label">4D<br>Ultrasound</div>
      </div>
      <div class="service">
        <svg class="service-icon" viewBox="0 0 54 54"><circle cx="27" cy="27" r="25" fill="none" stroke="var(--sage)" stroke-width="2"/><circle cx="23" cy="30" r="7" fill="none" stroke="var(--gold)" stroke-width="3"/><circle cx="31" cy="24" r="7" fill="none" stroke="var(--gold)" stroke-width="3"/><path d="M36 19l6-6M38 13h4v4M18 35l-6 6M12 38v3h3" fill="none" stroke="var(--gold)" stroke-width="3"/></svg>
        <div class="service-label">Early<br>Gender</div>
      </div>
      <div class="service">
        <svg class="service-icon" viewBox="0 0 54 54"><circle cx="27" cy="27" r="25" fill="none" stroke="var(--sage)" stroke-width="2"/><circle cx="27" cy="27" r="18" fill="none" stroke="var(--gold)" stroke-width="3"/></svg>
        <div class="service-label">Pregnancy<br>Confirmation</div>
      </div>
    </div>

    <div class="phone-pill">
      <svg class="phone-icon" viewBox="0 0 34 34"><path d="M8 4l5 6-3 3c1.5 4 5 7.5 9 9l3-3 6 5-3 5C14 28 6 20 3 8z" fill="#1c1c1c"/><path d="M21 6a9 9 0 0 1 7 7M21 1a14 14 0 0 1 12 12" fill="none" stroke="var(--gold-soft)" stroke-width="2"/></svg>
      <div class="phone-divider"></div>
      <div class="phone-number">850-471-5923</div>
    </div>

    <div class="headshot" role="img" aria-label="Professional headshot of the studio owner in green scrubs beside ultrasound equipment"></div>

    <div class="brand-card">
      <div class="brand-name">4D Little Lumen</div>
      <div class="brand-tagline">Prenatal Ultrasound Studio</div>
    </div>
  </section>
</div>
</body>
</html>
```